Brindlow Electrical Solutions needs a website

We need a new website designed because our current one is outdated. I would like a one-page website. We are a B2B company and want to maintain a professional appearance to appeal to project managers and directors.

for some reference, these are a few of my competitor's websites; we offer the same services.

https://valtorwiring.com.au/services
https://www.dunsary.com.au/mechanical-electrical-services/
https://www.gravik.com.au/

Industry/Entity Type

Electrical

Number of Pages Required

1 page

Font styles to use
Sans Serif

Colors
0054AA
0677BA
7BADD7
CADEEF
E8F1F8

```html
<!DOCTYPE html>
<html lang="en">
<head>
<meta charset="utf-8">
<title>Brindlow Electrical Solutions</title>
<link rel="stylesheet" href="https://fonts.googleapis.com/css2?family=Orbitron:wght@500;600;700;800&family=Poppins:wght@400;500&display=swap">
<style>
:root{
  --blue-deep:#0054AA;
  --blue:#0677BA;
  --blue-mid:#7BADD7;
  --blue-pale:#CADEEF;
  --blue-mist:#E8F1F8;
  --ink:#3a3a3a;
  --muted:#6b6b6b;
  --grey-band:#e7e7e7;
  --field:#e4e4e4;
  --dark:#2a2a2a;
  --topbar:#1f1f1f;
  --white:#ffffff;
}
*{margin:0;padding:0;box-sizing:border-box}
html,body{width:1200px;height:3301px;overflow:hidden;background:var(--white)}
body{font-family:"Poppins",sans-serif;color:var(--ink)}
.page{position:relative;width:1200px;height:3301px;overflow:hidden}
.abs{position:absolute}
.display{font-family:"Orbitron",sans-serif;text-transform:uppercase;letter-spacing:.5px}

/* top bar */
.topbar{left:276px;top:0;width:924px;height:38px;background:var(--topbar);clip-path:polygon(0 0,100% 0,100% 100%,36px 100%)}
.pill{top:6px;height:26px;border-radius:13px;background:linear-gradient(var(--blue),var(--blue-deep));color:var(--white);font-family:"Orbitron",sans-serif;font-size:12.5px;font-weight:600;display:flex;align-items:center;padding-left:4px;gap:12px}
.pill .dot{width:22px;height:22px;border-radius:50%;background:#1b2a3c;display:flex;align-items:center;justify-content:center}
.pill--phone{left:346px;width:154px}
.pill--mail{left:538px;width:298px}
.pill--pin{left:872px;width:238px}

/* header */
.header{left:0;top:38px;width:1200px;height:61px;background:var(--white)}
.brand{left:110px;top:28px;display:flex;align-items:center;gap:10px}
.brand-disc{width:56px;height:56px;border-radius:50%;background:var(--blue)}
.brand-name{font-family:"Orbitron",sans-serif;font-weight:700;font-size:17px;color:var(--blue);line-height:1.1}
.nav{top:60px;left:408px;display:flex;gap:25px;font-family:"Orbitron",sans-serif;font-size:13px;font-weight:600;color:#2f2f2f}

/* hero */
.hero{left:0;top:99px;width:1200px;height:659px;background:linear-gradient(110deg,#1d232b 0%,#3b454f 45%,#55606a 100%)}
.hero-photo{left:0;top:99px;width:1200px;height:659px;background:linear-gradient(160deg,#c9cdd1 0%,#8d959c 45%,#39414a 100%);clip-path:polygon(795px 0,1200px 0,1200px 659px,513px 659px)}
.hero-title{left:90px;top:252px;color:var(--white);font-family:"Orbitron",sans-serif;font-weight:800;font-size:46px;line-height:62px;letter-spacing:1px}
.hero-sub{left:90px;top:378px;width:540px;color:var(--white);font-family:"Orbitron",sans-serif;font-weight:600;font-size:13px;line-height:22px}
.btn{display:flex;align-items:center;justify-content:center;font-family:"Orbitron",sans-serif;font-weight:600;font-size:13px;color:var(--white);text-transform:uppercase}
.btn--solid{background:linear-gradient(var(--blue),var(--blue-deep))}
.btn--ghost{border:2px solid var(--white)}

/* who we are */
.about-band{left:0;top:758px;width:1200px;height:480px;background:var(--grey-band)}
.about-photo{left:151px;top:847px;width:417px;height:422px;background:linear-gradient(135deg,#d8dadc 0%,#9aa0a6 50%,#3c4248 100%)}
.section-title{font-family:"Orbitron",sans-serif;font-weight:700;font-size:27px;color:#444;text-transform:uppercase;letter-spacing:1px}
.about-title{left:613px;top:905px}
.about-copy{left:613px;top:953px;width:366px;font-size:12.4px;line-height:22.3px;color:#666}

/* services */
.services-title{left:0;top:1350px;width:1200px;text-align:center}
.svc-icon{width:70px;height:70px;border-radius:50%;background:linear-gradient(var(--blue),var(--blue-deep));display:flex;align-items:center;justify-content:center}
.svc{width:280px}
.svc h3{font-family:"Orbitron",sans-serif;font-weight:600;font-size:13.5px;color:#3a3a3a;text-transform:uppercase;margin-bottom:4px}
.svc p{font-size:11px;line-height:20px;color:#777}
.svc--left{text-align:right}

/* projects */
.projects-band{left:219px;top:1878px;width:762px;height:109px;background:linear-gradient(var(--blue) 0%,var(--blue-deep) 100%);color:var(--white);display:flex;align-items:center;justify-content:center;font-family:"Orbitron",sans-serif;font-weight:700;font-size:27px;letter-spacing:1px}
.tile{position:absolute}

/* contact */
.footer{left:0;top:2859px;width:1200px;height:382px;background:var(--dark)}
.contact-card{left:219px;top:2456px;width:762px;height:476px;background:var(--white);box-shadow:0 10px 40px rgba(0,0,0,.12)}
.contact-head{left:219px;top:2456px;width:762px;height:48px;background:linear-gradient(var(--blue),var(--blue-deep))}
.contact-title{left:0;top:2548px;width:1200px;text-align:center}
.field{position:absolute;background:var(--field);font-family:"Orbitron",sans-serif;font-weight:600;font-size:12.5px;color:#555;padding:10px 16px}

/* footer */
.foot-brand{left:0;top:2985px;width:1200px;display:flex;justify-content:center;align-items:center;gap:18px}
.foot-disc{width:70px;height:70px;border-radius:50%;background:var(--white)}
.foot-name{font-family:"Orbitron",sans-serif;font-weight:700;font-size:24px;color:var(--white);line-height:1.2}
.foot-nav{left:0;top:3104px;width:1200px;display:flex;justify-content:center;gap:24px;font-family:"Orbitron",sans-serif;font-weight:600;font-size:13px;color:var(--white)}
.social{top:3141px;width:50px;height:50px;border-radius:50%;border:2px solid var(--white)}
.social--filled{background:var(--blue);border-color:var(--blue)}
.copyright{left:0;top:3241px;width:1200px;height:60px;background:linear-gradient(var(--blue),var(--blue-deep));color:var(--white);display:flex;align-items:center;justify-content:center;font-family:"Orbitron",sans-serif;font-weight:600;font-size:12.5px}
</style>
</head>
<body>
<div class="page">

  <!-- top bar & header -->
  <div class="abs topbar"></div>
  <div class="abs pill pill--phone"><span class="dot"><svg width="12" height="12" viewBox="0 0 24 24"><path fill="#fff" d="M6.6 10.8a15.1 15.1 0 0 0 6.6 6.6l2.2-2.2c.3-.3.7-.4 1-.2 1.1.4 2.3.6 3.6.6.6 0 1 .4 1 1V20c0 .6-.4 1-1 1A17 17 0 0 1 3 4c0-.6.4-1 1-1h3.5c.6 0 1 .4 1 1 0 1.3.2 2.5.6 3.6.1.3 0 .7-.2 1z"/></svg></span>02 8011 4720</div>
  <div class="abs pill pill--mail"><span class="dot"><svg width="12" height="12" viewBox="0 0 24 24"><path fill="#fff" d="M2 5h20v14H2zm2 2v.5l8 5 8-5V7z"/></svg></span>info@brindlowsolutions.com.au</div>
  <div class="abs pill pill--pin"><span class="dot"><svg width="12" height="12" viewBox="0 0 24 24"><path fill="#fff" d="M12 2a7 7 0 0 0-7 7c0 5 7 13 7 13s7-8 7-13a7 7 0 0 0-7-7zm0 9.5A2.5 2.5 0 1 1 12 6.5a2.5 2.5 0 0 1 0 5z"/></svg></span>Sydney NSW, Australia</div>

  <div class="abs header"></div>
  <div class="abs brand">
    <span class="brand-disc"></span>
    <span class="brand-name">BRINDLOW<br><span style="font-size:10px;font-weight:600">ELECTRICAL SOLUTIONS</span></span>
  </div>
  <nav class="abs nav"><span>HOME</span><span>ABOUT US</span><span>SERVICES</span><span>WHY CHOOSE US</span><span>TESTIMONIALS</span><span>CONTACT US</span></nav>

  <!-- hero -->
  <div class="abs hero" role="img" aria-label="Technician working inside an electrical switchboard, dim industrial setting"></div>
  <div class="abs hero-photo" role="img" aria-label="Electrician in an orange hard hat and safety glasses inspecting equipment"></div>
  <h1 class="abs hero-title">MECHANICAL<br>ELECTRICAL HVAC</h1>
  <p class="abs hero-sub">DELIVERING INNOVATIVE, EFFICIENT, AND RELIABLE SOLUTIONS FOR COMMERCIAL AND INDUSTRIAL PROJECTS ACROSS AUSTRALIA.</p>
  <a class="abs btn btn--solid" style="left:90px;top:465px;width:202px;height:41px">Explore Services</a>
  <a class="abs btn btn--ghost" style="left:301px;top:465px;width:153px;height:41px">Contact Us</a>

  <!-- who we are -->
  <div class="abs about-band"></div>
  <div class="abs about-photo" role="img" aria-label="Electrician in a white hard hat working on a circuit breaker panel with pliers"></div>
  <h2 class="abs section-title about-title">Who We Are</h2>
  <p class="abs about-copy">At Brindlow Electrical Solutions, we specialize in delivering tailored mechanical, electrical, and HVAC solutions. With years of experience and a commitment to excellence, we partner with businesses to bring projects to life efficiently and professionally. From design to commissioning, we're trusted by project managers and directors across</p>
  <a class="abs btn btn--solid" style="left:613px;top:1108px;width:145px;height:41px">Read More</a>

  <!-- services -->
  <h2 class="abs section-title services-title">Our Services</h2>
  <svg class="abs" style="left:0;top:1380px" width="1200" height="400" viewBox="0 1380 1200 400">
    <defs>
      <radialGradient id="hubShade" cx="50%" cy="50%" r="50%">
        <stop offset="80%" stop-color="#ffffff"/>
        <stop offset="100%" stop-color="#e9e9e9"/>
      </radialGradient>
    </defs>
    <g stroke="#9a9a9a" stroke-width="1.2" fill="none">
      <line x1="384" y1="1429" x2="518" y2="1429"/>
      <line x1="673" y1="1429" x2="818" y2="1429"/>
      <line x1="384" y1="1565" x2="435" y2="1565"/>
      <line x1="756" y1="1565" x2="818" y2="1565"/>
      <line x1="384" y1="1718" x2="518" y2="1718"/>
      <line x1="673" y1="1718" x2="818" y2="1718"/>
      <circle cx="597" cy="1574" r="161" stroke="#777"/>
    </g>
    <circle cx="597" cy="1574" r="147" fill="url(#hubShade)"/>
    <g fill="#555">
      <circle cx="518" cy="1429" r="4"/><circle cx="673" cy="1429" r="4"/>
      <circle cx="435" cy="1565" r="4"/><circle cx="756" cy="1565" r="4"/>
      <circle cx="518" cy="1718" r="4"/><circle cx="673" cy="1718" r="4"/>
    </g>
  </svg>

  <!-- service icons -->
  <div class="abs svc-icon" style="left:314px;top:1388px"><svg width="34" height="34" viewBox="0 0 24 24" fill="none" stroke="#fff" stroke-width="1.4"><circle cx="12" cy="12" r="3"/><circle cx="4" cy="5" r="2"/><circle cx="20" cy="5" r="2"/><circle cx="4" cy="19" r="2"/><circle cx="20" cy="19" r="2"/><path d="M6 6l4 4M18 6l-4 4M6 18l4-4M18 18l-4-4"/></svg></div>
  <div class="abs svc-icon" style="left:314px;top:1532px"><svg width="34" height="34" viewBox="0 0 24 24" fill="none" stroke="#fff" stroke-width="1.4"><rect x="3" y="4" width="14" height="16" rx="1"/><circle cx="10" cy="12" r="3"/><path d="M15 15l6 6"/></svg></div>
  <div class="abs svc-icon" style="left:314px;top:1683px"><svg width="34" height="34" viewBox="0 0 24 24" fill="none" stroke="#fff" stroke-width="1.4"><path d="M9 18h6M10 21h4M12 3a6 6 0 0 0-4 10.5c.7.7 1 1.5 1 2.5h6c0-1 .3-1.8 1-2.5A6 6 0 0 0 12 3z"/><circle cx="12" cy="9" r="2"/></svg></div>
  <div class="abs svc-icon" style="left:818px;top:1388px"><svg width="34" height="34" viewBox="0 0 24 24" fill="none" stroke="#fff" stroke-width="1.4"><rect x="4" y="3" width="13" height="18" rx="1"/><path d="M7 8h7M7 12h7M7 16h4"/><circle cx="18" cy="17" r="3.5"/><path d="M16.5 17l1 1 2-2"/></svg></div>
  <div class="abs svc-icon" style="left:818px;top:1532px"><svg width="34" height="34" viewBox="0 0 24 24" fill="none" stroke="#fff" stroke-width="1.4"><path d="M3 21V11l5 3V11l5 3V6h3v3h2V4h3v17z"/><path d="M3 21h18"/></svg></div>
  <div class="abs svc-icon" style="left:818px;top:1683px"><svg width="34" height="34" viewBox="0 0 24 24" fill="none" stroke="#fff" stroke-width="1.4"><circle cx="14" cy="12" r="4"/><path d="M14 5v2M14 17v2M7 12h2M19 12h2"/><path d="M5 4c0 2-2 3-2 5a2 2 0 0 0 4 0c0-2-2-3-2-5zM6 16l-3 3M3 16l3 3"/></svg></div>

  <div class="abs svc svc--left" style="left:25px;top:1396px"><h3>Commissioning</h3><p>Thorough testing and verification to<br>guarantee systems are fully operational.</p></div>
  <div class="abs svc svc--left" style="left:25px;top:1537px"><h3>Engineering</h3><p>Practical engineering solutions ensuring<br>performance, safety, and compliance.</p></div>
  <div class="abs svc svc--left" style="left:25px;top:1686px"><h3>Project Management</h3><p>Streamlined project delivery with expert<br>planning and clear communication.</p></div>
  <div class="abs svc" style="left:897px;top:1396px"><h3>Project Design</h3><p>Innovative designs combining func-<br>tionality, efficiency, and sustainability.</p></div>
  <div class="abs svc" style="left:897px;top:1537px"><h3>Industrial Projects</h3><p>Tailored solutions for large-scale indus-<br>trial and commercial developments.</p></div>
  <div class="abs svc" style="left:897px;top:1686px"><h3>BMCS &amp; HVAC</h3><p>Advanced climate control and building<br>management systems for energy...</p></div>

  <!-- projects -->
  <div class="abs projects-band">OUR PROJECTS</div>
  <div class="tile" style="left:0;top:1993px;width:363px;height:355px;background:linear-gradient(135deg,#c8ccd0,#5a6470 60%,#1e242b)" role="img" aria-label="Technician with a tablet checking a switchboard"></div>
  <div class="tile" style="left:369px;top:1993px;width:230px;height:175px;background:linear-gradient(160deg,#9a9896,#6b6661 60%,#4a4743)" role="img" aria-label="Wall-mounted electrical distribution boards in a plant room"></div>
  <div class="tile" style="left:369px;top:2174px;width:230px;height:174px;background:linear-gradient(170deg,#a9c6dd,#6e93ad 50%,#6f8f5a)" role="img" aria-label="Modern glass and steel commercial building walkway"></div>
  <div class="tile" style="left:604px;top:1993px;width:231px;height:175px;background:linear-gradient(135deg,#e4e6e8,#8a9096 55%,#2e3338)" role="img" aria-label="Engineer wiring industrial control equipment"></div>
  <div class="tile" style="left:604px;top:2174px;width:231px;height:174px;background:linear-gradient(135deg,#9aa4ae,#3a5a8a 55%,#1f2d45)" role="img" aria-label="Two engineers in hard hats reviewing data on a laptop"></div>
  <div class="tile" style="left:840px;top:1993px;width:360px;height:355px;background:linear-gradient(160deg,#d8d8d8,#a3a3a3 50%,#2c2c2c)" role="img" aria-label="Linear pendant lighting installed in a modern interior"></div>

  <!-- contact -->
  <div class="abs footer"></div>
  <div class="abs contact-card"></div>
  <div class="abs contact-head"></div>
  <h2 class="abs section-title contact-title">Contact Us</h2>
  <div class="field" style="left:264px;top:2625px;width:328px;height:33px">NAME*</div>
  <div class="field" style="left:603px;top:2625px;width:329px;height:33px">EMAIL*</div>
  <div class="field" style="left:264px;top:2678px;width:328px;height:32px">PHONE*</div>
  <div class="field" style="left:603px;top:2678px;width:329px;height:32px">PROJECT*</div>
  <div class="field" style="left:264px;top:2731px;width:668px;height:102px">MESSAGE*</div>
  <a class="abs btn btn--solid" style="left:519px;top:2852px;width:162px;height:40px">Submit Now</a>

  <!-- footer -->
  <div class="abs foot-brand">
    <span class="foot-disc"></span>
    <span class="foot-name">BRINDLOW<br><span style="font-size:15px">ELECTRICAL SOLUTIONS</span></span>
  </div>
  <nav class="abs foot-nav"><span>HOME</span><span>ABOUT US</span><span>SERVICES</span><span>WHY CHOOSE US</span><span>TESTIMONIALS</span><span>CONTACT US</span></nav>
  <span class="abs social social--filled" style="left:498px" aria-label="Social profile"></span>
  <span class="abs social" style="left:562px" aria-label="Social profile"></span>
  <span class="abs social" style="left:625px" aria-label="Social profile"></span>
  <div class="abs copyright">© COPYRIGHT 2021 BRINDLOW ELECTRICAL SOLUTIONS | ALL RIGHTS RESERVED</div>

</div>
</body>
</html>
```